Online-Marketing Material für Bewegungsangebot speziell für Kinder
Zielgruppe
Hopsalino bietet ein hochwertiges, sportwissenschaftlich fundiertes Bewegungsangebot speziell für Kinder an. Unsere Kurse verbinden spielerische Elemente mit modernen Trainingsmethoden und schaffen eine liebevolle Umgebung in der Kinder ganz ohne Druck wachsen, lernen und sich mit Freude bewegen.
Unsere Zielgruppe sind Eltern mit Kindern zwischen zwei und acht Jahren, die ein qualitativ sehr hochwertiges Sportprogramm für ihre Kinder suchen und großen Wert auf professionelle Förderung, Sicherheit und eine warmherzige Atmosphäre legen.
Aufgabenstellung
Die Kreativen sollen berücksichtigen, dass der neue Hero ein echter Eye Catcher sein muss. Er soll sofort ein Wow-Gefühl auslösen und viel stärker auffallen als die aktuelle, eher schlichte Hero Section. Die Gestaltung soll hochwertig, kindlich liebevoll und gleichzeitig modern wirken. Der neue Hero muss sich perfekt in das bestehende Webdesign einfügen und die Hopsalino Welt auf den ersten Blick spürbar machen. Der bestehende Text bleibt zwingend erhalten. Alles andere darf kreativ neu gedacht werden, solange das Ergebnis direkt Aufmerksamkeit fängt, Emotionen weckt und die hohe Qualität des Sportangebots im Kindersegment sichtbar macht.
Ich benötige ein vollständiges Redesign ausschließlich für die Hero Section meiner Website www.hopsalino-kurse.example. Das restliche Webdesign passt bereits sehr gut zu meiner Marke, doch die aktuelle Hero Section wirkt noch zu schlicht und erzeugt kein echtes Wow-Gefühl.
Hopsalino steht für ein hochwertiges, sportwissenschaftlich fundiertes Sportangebot für Kinder zwischen zwei und acht Jahren. Unsere Welt ist liebevoll, warm, spielerisch und gleichzeitig sehr professionell. Genau dieses Gefühl soll der neue Hero sofort transportieren.
Wichtige Vorgaben
• Es geht ausschließlich um die Hero Section
• Der bestehende Text muss unbedingt erhalten bleiben
• Das Design soll hochwertig, kindlich, warm und liebevoll wirken
• Optisch nahtlose Anpassung an das bestehende Webdesign
• Der neue Hero soll ein klarer Eye Catcher sein und ein echtes Wow erzeugen
• Kreative Freiheit in der Gestaltung, solange alles modern, hochwertig und zur Hopsalino Welt passend bleibt
Mir ist wichtig, dass der neue Hero direkt Emotionen weckt und die hohe Qualität unseres Kinder-Sportangebots schon auf den ersten Blick spürbar macht.

```html
<!DOCTYPE html>
<html lang="de">
<head>
<meta charset="utf-8">
<title>Hopsalino – Ballschule für Kinder</title>
<link href="https://fonts.googleapis.com/css2?family=Fira+Sans:wght@300;400;500;600&display=swap" rel="stylesheet">
<style>
  :root{
    --sky:#38c6f4;
    --sky-deep:#1a9fd6;
    --sky-soft:#a9e3f8;
    --gold:#c99a3a;
    --gold-light:#ecd27c;
    --sand:#f3d77a;
    --white:#ffffff;
    --ink:#3a3f46;
    --mint:#9fd9b8;
    --bg:#eef1f3;
  }
  *{box-sizing:border-box;margin:0;padding:0}
  html,body{width:1200px;height:800px;overflow:hidden;background:var(--bg)}
  body{font-family:"Fira Sans",sans-serif;color:var(--ink)}
  .page{position:relative;width:1200px;height:800px;overflow:hidden;background:var(--sky)}

  .topbar{height:30px;background:linear-gradient(90deg,var(--gold) 0%,var(--gold-light) 30%,var(--sand) 50%,var(--gold-light) 75%,var(--gold) 100%);
    display:flex;align-items:center;padding:0 70px;font-size:12px;color:var(--white);font-weight:300}
  .topbar .contact{display:flex;gap:26px;align-items:center}
  .topbar .contact span{display:flex;gap:6px;align-items:center}
  .topbar .promo{margin-left:auto;font-weight:400}

  .nav{height:72px;background:var(--white);display:flex;align-items:center;padding:0 70px;position:relative;z-index:2}
  .brand{display:flex;align-items:center;gap:8px;font-weight:600;font-size:17px;color:var(--ink)}
  .brand .dot{width:26px;height:26px;border-radius:50%;background:var(--gold)}
  .menu{display:flex;gap:30px;margin-left:280px;font-size:14px;font-weight:300;color:var(--ink)}
  .cta-small{margin-left:auto;background:linear-gradient(90deg,var(--gold),var(--gold-light));color:var(--white);
    font-size:13px;padding:9px 16px;border-radius:18px;box-shadow:0 4px 10px rgba(0,0,0,.12)}

  .hero{position:absolute;top:102px;left:0;width:1200px;height:698px}
  .glow{position:absolute;left:520px;top:40px;width:520px;height:420px;border-radius:50%;
    background:radial-gradient(circle,rgba(243,215,122,.75) 0%,rgba(243,215,122,.25) 40%,rgba(56,198,244,0) 70%)}
  .copy{position:absolute;left:90px;top:120px;width:520px;color:var(--white)}
  .pill{display:inline-block;background:var(--white);color:var(--gold);font-size:12px;padding:7px 12px;border-radius:14px}
  .headline-wrap{position:relative}
  .headline{font-weight:400;font-size:52px;line-height:1.2;margin-top:14px;letter-spacing:-.5px}
  .spark-accent{position:absolute;left:458px;top:18px;width:70px;height:60px;border-radius:50%;
    background:radial-gradient(circle,rgba(243,215,122,.85) 0%,rgba(243,215,122,.35) 45%,rgba(243,215,122,0) 70%)}
  .swoosh{display:block;margin-top:14px;width:520px;height:10px;border-radius:5px;
    background:linear-gradient(90deg,var(--sand),var(--gold-light))}
  .lead{font-size:14px;font-weight:300;line-height:1.6;margin-top:26px;width:460px}
  .lead strong{font-weight:600}
  .actions{display:flex;align-items:center;gap:14px;margin-top:26px}
  .cta{background:linear-gradient(90deg,var(--gold),var(--gold-light));color:var(--white);font-size:14px;
    padding:11px 18px;border-radius:20px;box-shadow:0 5px 12px rgba(0,0,0,.15);letter-spacing:.3px}
  .icons{display:flex}
  .icons span{width:34px;height:34px;border-radius:50%;border:1.5px solid var(--white);background:rgba(255,255,255,.25);
    margin-left:-6px;display:flex;align-items:center;justify-content:center}
  .icons span:first-child{margin-left:0}
  .proof{font-size:13px;font-weight:500}

  .features{position:absolute;left:110px;top:560px;display:flex;gap:34px;color:var(--white);font-size:13px;font-weight:500}
  .features span{display:flex;align-items:center;gap:8px}
  .tick{width:24px;height:24px;border-radius:50%;background:rgba(255,255,255,.35);display:flex;align-items:center;justify-content:center}

  .gallery{position:absolute;left:640px;top:90px;width:480px;height:450px}
  .photo{position:absolute;border-radius:14px;box-shadow:0 10px 24px rgba(0,0,0,.15)}
  .photo.main{left:0;top:0;width:470px;height:260px;background:linear-gradient(135deg,#9aa3a8,#6b8aa6 55%,#2a6fc2)}
  .photo.court{left:30px;top:275px;width:225px;height:185px;background:linear-gradient(160deg,#7f9aa3,#2d6fb8 50%,#e7c443)}
  .photo.coach{left:265px;top:265px;width:220px;height:185px;background:linear-gradient(160deg,#8b6a50,#b7a08a 35%,#1e6fd0)}
  .age{position:absolute;left:400px;top:-30px;width:58px;height:58px;border-radius:50%;background:var(--white);
    display:flex;flex-direction:column;align-items:center;justify-content:center;font-size:9px;color:var(--ink);box-shadow:0 4px 10px rgba(0,0,0,.12)}
  .age .ball{width:16px;height:16px;border-radius:50%;border:2px solid var(--ink);margin-bottom:3px}
  .bubble{position:absolute;border-radius:50%}
  .b1{left:1000px;top:310px;width:54px;height:54px;background:var(--sky-deep);opacity:.5}
  .b2{left:625px;top:480px;width:80px;height:80px;background:var(--sky-soft);opacity:.8}
  .b3{left:990px;top:60px;width:44px;height:44px;background:var(--mint);opacity:.7}
  .wave{position:absolute;left:0;bottom:0}
</style>
</head>
<body>
<div class="page">
  <div class="topbar">
    <div class="contact">
      <span><svg width="12" height="12" viewBox="0 0 24 24" fill="none" stroke="#fff" stroke-width="2"><path d="M5 3h4l2 5-3 2a11 11 0 0 0 6 6l2-3 5 2v4a2 2 0 0 1-2 2A17 17 0 0 1 3 5a2 2 0 0 1 2-2z"/></svg>+49 (0) 987 654321</span>
      <span><svg width="13" height="12" viewBox="0 0 24 20" fill="none" stroke="#fff" stroke-width="2"><rect x="2" y="2" width="20" height="16" rx="2"/><path d="M2 4l10 7 10-7"/></svg>info@hopsalino-kurse.example</span>
    </div>
    <div class="promo">Kostenlose Probestunde sichern!</div>
  </div>

  <nav class="nav">
    <div class="brand"><span class="dot"></span>Hopsalino</div>
    <div class="menu"><span>Kurse</span><span>Über uns</span><span>Trainer</span><span>Standorte</span><span>Kontakt</span></div>
    <div class="cta-small">Jetzt anmelden ♡</div>
  </nav>

  <section class="hero">
    <div class="glow"></div>
    <div class="bubble b3"></div>
    <div class="bubble b1"></div>
    <div class="bubble b2"></div>

    <div class="copy">
      <span class="pill">Sportwissenschaftlich fundiert</span>
      <div class="headline-wrap">
        <h1 class="headline">Deine Ballschule für<br>Kinder ab 2 Jahren</h1>
        <div class="spark-accent" role="img" aria-label="Kleine gezeichnete Strahlen als Akzent"></div>
      </div>
      <div class="swoosh" role="img" aria-label="Handgezeichneter gelber Pinselstrich unter der Überschrift"></div>
      <p class="lead">Stinkbomben ausweichen, Balli retten und ins Weltall fliegen. Bei Hopsalino werden Kinder nicht nur zu kleinen Bewegungsprofis, bei uns geht es um weit mehr. <strong>Motorik, Koordination und gezieltes Gehirntraining fördern</strong> die Entwicklung deines Kindes spielerisch und ganzheitlich in einer liebevollen Umgebung.</p>
      <div class="actions">
        <span class="cta">JETZT STARTEN ☆</span>
        <div class="icons">
          <span><svg width="14" height="14" viewBox="0 0 24 24" fill="none" stroke="#fff" stroke-width="2"><path d="M12 21s-8-5-8-11a4 4 0 0 1 8-1 4 4 0 0 1 8 1c0 6-8 11-8 11z"/></svg></span>
          <span><svg width="14" height="14" viewBox="0 0 24 24" fill="none" stroke="#fff" stroke-width="2"><circle cx="12" cy="12" r="9"/><path d="M3 12h18M12 3v18"/></svg></span>
          <span><svg width="14" height="14" viewBox="0 0 24 24" fill="none" stroke="#fff" stroke-width="2"><path d="M12 3l2.7 5.6 6.1.9-4.4 4.3 1 6.1L12 17l-5.4 2.9 1-6.1-4.4-4.3 6.1-.9z"/></svg></span>
        </div>
        <span class="proof">Über 500 glückliche Kinder</span>
      </div>
    </div>

    <div class="gallery">
      <div class="photo main" role="img" aria-label="Foto: Trainer wirft einem lachenden Kleinkind einen kleinen Ball zu"></div>
      <div class="photo court" role="img" aria-label="Foto: Kinder üben auf einem blauen Sportplatz mit gelben Hütchen"></div>
      <div class="photo coach" role="img" aria-label="Foto: Trainer im blauen Vereinsshirt von hinten"></div>
      <div class="age"><span class="ball"></span>2-8 Jahre</div>
    </div>

    <div class="features">
      <span><i class="tick"><svg width="12" height="12" viewBox="0 0 24 24" fill="none" stroke="#fff" stroke-width="3"><path d="M4 12l5 5 11-11"/></svg></i>Qualifizierte Trainer</span>
      <span><i class="tick"><svg width="12" height="12" viewBox="0 0 24 24" fill="none" stroke="#fff" stroke-width="3"><path d="M4 12l5 5 11-11"/></svg></i>Altersgerechte Kurse</span>
      <span><i class="tick"><svg width="12" height="12" viewBox="0 0 24 24" fill="none" stroke="#fff" stroke-width="3"><path d="M4 12l5 5 11-11"/></svg></i>Spielerisch Lernen</span>
    </div>

    <svg class="wave" width="1200" height="110" viewBox="0 0 1200 110" preserveAspectRatio="none">
      <path d="M0 110 C300 40 800 10 1200 0 L1200 110 Z" fill="var(--white)"/>
    </svg>
  </section>
</div>
</body>
</html>
```